Stationary for Vornik Consulting

Hi

I am after stationary designs for my company - Vornik Consulting. I have a logo - recently designed by PixelHarbor. Vornik ( sales spelt backwards ) is a sales consultancy - including sales training, sales coaching and business management.

I have attached some of the artwork I already have, as well as a few ideas
1. Use supplied logo's
2. back of business card to use the logo with the dark background and white text
3. details to be included on card are
Logo
Delmo Kastrani
p: +61409371826
e: delmo@vornikconsulting.com.au
w: www.vornikconsulting.com.au
PO Box 417, Fernleigh East, Larkdale, 2906

4. I am after designs for business cards, A4 letterhead and A5 letterhead

Thanks in Advance

Delmo

```html
<!DOCTYPE html>
<html lang="en">
<head>
<meta charset="UTF-8">
<title>Vornik Consulting – Business Card</title>
<link href="https://fonts.googleapis.com/css2?family=Open+Sans:wght@400;600;700&display=swap" rel="stylesheet">
<style>
  :root {
    --slate: #2f424d;
    --accent: #e0522a;
    --paper: #ffffff;
    --ink: #2b2b2b;
    --backdrop: #e4e3e0;
  }
  * { margin: 0; padding: 0; box-sizing: border-box; }
  html, body { width: 1200px; height: 900px; overflow: hidden; }
  body {
    background: var(--backdrop);
    font-family: "Open Sans", Arial, sans-serif;
    position: relative;
  }
  .card { position: absolute; box-shadow: 0 6px 18px rgba(0,0,0,.18); }

  /* Back of card */
  .card-back {
    left: 70px; top: 270px; width: 630px; height: 360px;
    background: var(--slate);
    display: flex; align-items: center; justify-content: center;
  }
  .brand-back {
    color: var(--paper); font-weight: 700; font-size: 54px;
    letter-spacing: 2px; text-align: center; line-height: 1.1;
  }
  .brand-back span { display: block; font-size: 20px; letter-spacing: 12px; margin-top: 6px; }

  /* Front of card */
  .card-front {
    left: 790px; top: 135px; width: 360px; height: 630px;
    background: var(--paper); overflow: hidden;
  }
  .panel { position: absolute; left: 0; width: 360px; }
  .panel-top { top: 0; height: 150px; }
  .panel-bottom { bottom: 0; height: 150px; }
  .panel-text {
    position: absolute; left: 0; width: 360px; text-align: center;
    color: var(--paper);
  }
  .holder-name {
    top: 52px; font-size: 19px; font-weight: 600; letter-spacing: 3px;
    text-transform: uppercase;
  }
  .tagline { bottom: 48px; font-size: 18px; }

  .brand-front {
    position: absolute; top: 178px; left: 0; width: 360px; text-align: center;
    color: var(--slate); font-weight: 700; font-size: 38px; line-height: 1.1;
  }
  .brand-front span { display: block; font-size: 15px; letter-spacing: 9px; margin-top: 4px; }

  .contact {
    position: absolute; top: 290px; left: 40px; width: 280px;
    color: var(--ink); font-size: 13.5px;
  }
  .contact-row {
    display: flex; align-items: center; gap: 8px;
    padding: 8px 0; border-bottom: 2px solid var(--accent);
  }
  .contact-row svg { width: 14px; height: 14px; flex: none; }
  .contact-stack { flex-direction: column; align-items: flex-start; gap: 0; }
  .contact-stack .line { display: flex; align-items: center; gap: 8px; padding: 2px 0; }
</style>
</head>
<body>

<section class="card card-back" aria-label="Business card back">
  <div class="brand-back">Vornik<span>CONSULTING</span></div>
</section>

<section class="card card-front" aria-label="Business card front">
  <svg class="panel panel-top" viewBox="0 0 360 150" aria-hidden="true">
    <polygon points="30,0 330,0 330,105 290,140 70,140 30,105" fill="var(--slate)" stroke="var(--accent)" stroke-width="2"/>
  </svg>
  <div class="panel-text holder-name">Delmo Kastrani</div>

  <div class="brand-front">Vornik<span>CONSULTING</span></div>

  <div class="contact">
    <div class="contact-row">PO Box 417, Fernleigh East, Larkdale, 2906</div>
    <div class="contact-row">
      <svg viewBox="0 0 14 14" aria-hidden="true"><path d="M3 1h3l1 3-2 1.5a7 7 0 0 0 3.5 3.5L10 7l3 1v3a2 2 0 0 1-2 2A10 10 0 0 1 1 3a2 2 0 0 1 2-2z" fill="var(--accent)"/></svg>
      +61409371826
    </div>
    <div class="contact-row contact-stack">
      <div class="line">
        <svg viewBox="0 0 14 14" aria-hidden="true"><rect x="1" y="3" width="12" height="8" fill="none" stroke="var(--accent)" stroke-width="1.3"/><path d="M1 3l6 5 6-5" fill="none" stroke="var(--accent)" stroke-width="1.3"/></svg>
        delmo@vornikconsulting.com.au
      </div>
      <div class="line">
        <svg viewBox="0 0 14 14" aria-hidden="true"><circle cx="7" cy="7" r="5.5" fill="none" stroke="var(--accent)" stroke-width="1.3"/><ellipse cx="7" cy="7" rx="2.5" ry="5.5" fill="none" stroke="var(--accent)" stroke-width="1"/><path d="M1.5 7h11" stroke="var(--accent)" stroke-width="1"/></svg>
        www.vornikconsulting.com.au
      </div>
    </div>
  </div>

  <svg class="panel panel-bottom" viewBox="0 0 360 150" aria-hidden="true">
    <polygon points="70,10 290,10 330,45 330,150 30,150 30,45" fill="var(--slate)" stroke="var(--accent)" stroke-width="2"/>
  </svg>
  <div class="panel-text tagline">Your Business is Our Business</div>
</section>

</body>
</html>
```